The Bright Lantern, an online college fair for non-traditional students, needs a web site

I need design and coding for a functioning web site that will serve as an online college fair that connects non-traditional students with college admissions officers and college advisors. I have chosen Wordpress and the "Meridian" theme for the site, and you can see what I already have here: https://brightlanternhub.example/
I need help setting up the site's pages and functionality, including SEO optimization and a password protected area. I will manage all content. In addition to me as the administrator, other users will be: college admissions officers, non-traditional students (like homeschoolers), and college advisors.
Target Market(s)
Homeschoolers and college/university admissions officers
Industry/Entity Type
College
Coding
Coded - Design and coding required
Number of Pages Required
5+ page
Font styles to use
Requirements
Must have
- - An inviting but professional look (see the logo as a starting point)
- - Easy to navigate
- - A way to register subscribed members (students)
- - A password-protected "members only" area
- - Virtual "booths" on the Schools page that lead to a detail page for each school
- - SEO optimized
Nice to have
- - Searchable site

```html
<!DOCTYPE html>
<html lang="en">
<head>
<meta charset="utf-8">
<title>The Bright Lantern – Virtual College Fair</title>
<link href="https://fonts.googleapis.com/css2?family=Roboto:wght@400;500;700&family=Roboto+Condensed:wght@400;700&family=Open+Sans:ital,wght@0,400;0,600;1,400&display=swap" rel="stylesheet">
<style>
:root{
  --navy:#0f2b52;
  --navy-deep:#0a2142;
  --red:#d0121b;
  --ink:#222;
  --muted:#555;
  --light:#f3f3f3;
  --white:#fff;
  --line:#e3e3e3;
}
*{box-sizing:border-box;margin:0;padding:0}
html,body{width:1200px;height:2965px;overflow:hidden}
body{font-family:"Open Sans",Arial,sans-serif;color:var(--ink);background:var(--white);position:relative}
.abs{position:absolute}
h2.section-title{position:absolute;left:0;width:1200px;text-align:center;font-family:"Roboto",Arial,sans-serif;font-weight:400;font-size:30px;color:var(--ink);letter-spacing:.5px}

/* header */
.site-header{position:absolute;top:0;left:0;width:1200px;height:133px;background:var(--white)}
.brand{position:absolute;left:99px;top:40px;display:flex;align-items:center;gap:12px}
.brand-mark{width:46px;height:46px;background:var(--red)}
.brand-name{font-family:"Roboto",Arial,sans-serif;font-weight:700;font-size:22px;color:var(--navy);line-height:1}
.brand-tag{position:absolute;left:157px;top:72px;font-size:9px;color:var(--navy)}
.search{position:absolute;left:664px;top:46px;width:234px;height:36px;border:1px solid #ccc;display:flex}
.search span{flex:1;font-size:11px;color:#777;padding:10px 12px}
.search i{width:36px;background:#e6e6e6;border-left:1px solid #ccc;display:flex;align-items:center;justify-content:center}
.btn-outline{position:absolute;top:46px;height:36px;border:2px solid var(--navy);font-size:12px;color:var(--navy);display:flex;align-items:center;gap:7px;padding:0 12px;font-family:"Roboto",Arial,sans-serif}
.btn-login{left:918px;width:78px}
.btn-register{left:1007px;width:93px}

/* nav */
.main-nav{position:absolute;top:133px;left:0;width:1200px;height:49px;background:var(--navy);display:flex;padding-left:99px}
.main-nav a{color:var(--white);text-decoration:none;font-family:"Roboto",Arial,sans-serif;font-size:13px;display:flex;align-items:center;padding:0 30px;border-right:1px solid rgba(255,255,255,.12)}
.main-nav a.active{background:var(--red)}

/* hero */
.hero{position:absolute;top:182px;left:0;width:1200px;height:550px;overflow:hidden}
.hero-photo{position:absolute;inset:0;background:linear-gradient(90deg,#6a4e37 0%,#9a7b5c 35%,#c7b3a0 60%,#8a6f59 100%)}
.hero-copy{position:absolute;left:113px;top:160px;width:470px;color:var(--white)}
.hero-copy h1{font-family:"Roboto Condensed",Arial,sans-serif;font-weight:700;font-size:42px;line-height:44px}
.hero-copy p{font-size:13px;line-height:21px;margin-top:10px}
.hero-btn{display:inline-flex;align-items:center;gap:6px;margin-top:18px;background:var(--navy);color:var(--white);font-size:13px;padding:11px 18px;border-radius:3px;font-family:"Roboto",Arial,sans-serif}
.hero-arrow{position:absolute;top:228px;width:30px;height:30px;border-radius:50%;background:rgba(0,0,0,.3);display:flex;align-items:center;justify-content:center}
.hero-curve{position:absolute;left:0;top:460px}

/* services */
.services{position:absolute;top:732px;left:0;width:1200px;height:460px;background:#f8f8f8}
.service{position:absolute;top:112px;width:310px}
.service .thumb{width:310px;height:182px}
.service h3{font-family:"Roboto",Arial,sans-serif;font-weight:400;font-size:18px;margin-top:20px}
.service p{font-size:11px;line-height:21px;color:var(--muted);margin-top:8px}

/* how it works */
.how{position:absolute;top:1192px;left:0;width:1200px;height:522px;background:var(--white)}
.step{position:absolute;top:146px;width:230px;text-align:center}
.step svg{display:block;margin:0 auto}
.step h3{font-family:"Roboto",Arial,sans-serif;font-weight:400;font-size:17px;margin-top:22px}
.step p{font-size:11px;line-height:21px;color:var(--muted);margin-top:12px}
.step .more{display:block;font-family:"Roboto",Arial,sans-serif;font-size:11px;color:var(--ink);margin-top:12px;font-weight:500}

/* testimonial */
.testimonial{position:absolute;top:1714px;left:0;width:1200px;height:269px;background:var(--light)}
.avatar{position:absolute;left:170px;top:60px;width:120px;height:120px;border-radius:50%;background:linear-gradient(160deg,#d8c2ad,#a88468);border:4px solid var(--white)}
.quote{position:absolute;left:314px;top:76px;width:740px;font-style:italic;font-size:12.5px;line-height:24px;color:var(--muted)}
.quote-name{position:absolute;left:314px;top:156px;font-style:italic;font-weight:600;font-size:14px;color:var(--navy)}
.dots{position:absolute;left:314px;top:203px;display:flex;gap:6px}
.dots span{width:24px;height:3px;background:#ccc}
.dots span:first-child{background:var(--navy)}
.quote-mark{position:absolute;left:995px;top:145px;font-family:Georgia,serif;font-size:90px;color:#dcdcdc;line-height:1}

/* news */
.news{position:absolute;top:1983px;left:0;width:1200px;height:627px;background:var(--white)}
.card{position:absolute;top:142px;width:458px;padding-bottom:18px;border-bottom:1px solid var(--line)}
.card .thumb{width:458px;height:261px}
.card h3{font-family:"Roboto Condensed",Arial,sans-serif;font-weight:400;font-size:19px;margin-top:22px}
.card .meta{font-size:11px;color:var(--muted);margin-top:10px;display:flex;align-items:center;gap:7px}
.card p{font-size:11px;line-height:22px;color:var(--muted);margin-top:10px}

/* footer */
.site-footer{position:absolute;top:2610px;left:0;width:1200px;height:355px;background:linear-gradient(180deg,#14335e,var(--navy-deep));color:var(--white)}
.f-col{position:absolute;top:40px}
.f-col h4{font-family:"Roboto",Arial,sans-serif;font-weight:500;font-size:17px;letter-spacing:.3px}
.f-links{list-style:none;margin-top:26px}
.f-links li{font-size:12px;line-height:26px;display:flex;align-items:center;gap:10px}
.f-contact{margin-top:26px;font-size:12px;line-height:20px}
.f-contact div{display:flex;gap:14px;margin-bottom:18px}
.f-news p{font-size:12px;line-height:20px;margin-top:16px;width:220px}
.f-input{width:286px;height:40px;background:var(--white);color:#777;font-size:11px;padding:13px 14px;margin-top:14px}
.f-btn{display:inline-block;background:var(--red);font-size:12px;padding:12px 16px;margin-top:16px;font-family:"Roboto",Arial,sans-serif}
.f-social li{gap:12px;line-height:36px;font-size:13px}
.f-social i{width:26px;height:26px;border:1.5px solid var(--white);border-radius:50%;display:inline-block}
.copyright{position:absolute;top:324px;left:0;width:1200px;text-align:center;font-size:12px}
</style>
</head>
<body>

<header class="site-header">
  <div class="brand"><span class="brand-mark"></span><span class="brand-name">THE BRIGHT LANTERN</span></div>
  <div class="brand-tag">A Virtual College Fair for Non-Traditional Students</div>
  <div class="search"><span>Search</span><i><svg width="13" height="13" viewBox="0 0 13 13"><circle cx="5.5" cy="5.5" r="4" fill="none" stroke="#444" stroke-width="1.6"/><line x1="8.5" y1="8.5" x2="12" y2="12" stroke="#444" stroke-width="1.6"/></svg></i></div>
  <div class="btn-outline btn-login"><svg width="11" height="12" viewBox="0 0 11 12"><circle cx="5.5" cy="3" r="3" fill="#0f2b52"/><path d="M0 12a5.5 5 0 0 1 11 0z" fill="#0f2b52"/></svg>Login</div>
  <div class="btn-outline btn-register"><svg width="11" height="12" viewBox="0 0 11 12"><circle cx="5.5" cy="3" r="3" fill="#0f2b52"/><path d="M0 12a5.5 5 0 0 1 11 0z" fill="#0f2b52"/></svg>Register</div>
</header>

<nav class="main-nav">
  <a class="active">HOME</a><a>STUDENTS</a><a>SCHOOLS</a><a>ADVISORS</a><a>MEMBER RESOURCES</a><a>NEWS</a><a>CONTACT US</a>
</nav>

<section class="hero">
  <div class="hero-photo" role="img" aria-label="Student using a tablet in a library"></div>
  <div class="hero-copy">
    <h1>NON-TRADITIONAL<br>STUDENTS</h1>
    <p>Sed ut perspiciatis unde omnis iste natus error sit voluptatem accusantium doloremque laudantium, totam</p>
    <span class="hero-btn">READ MORE <svg width="11" height="11" viewBox="0 0 11 11"><circle cx="5.5" cy="5.5" r="5.5" fill="#fff"/><path d="M4.3 3l2.5 2.5-2.5 2.5" stroke="#0f2b52" stroke-width="1.5" fill="none"/></svg></span>
  </div>
  <div class="hero-arrow" style="left:40px"><svg width="10" height="14"><path d="M8 1L2 7l6 6" stroke="#fff" stroke-width="2" fill="none"/></svg></div>
  <div class="hero-arrow" style="left:1130px"><svg width="10" height="14"><path d="M2 1l6 6-6 6" stroke="#fff" stroke-width="2" fill="none"/></svg></div>
  <svg class="hero-curve" width="1200" height="90" viewBox="0 0 1200 90">
    <path d="M0 14 Q300 62 600 88 Q900 50 1200 0 L1200 90 L0 90Z" fill="#f8f8f8"/>
    <path d="M0 14 Q300 62 600 88 Q900 50 1200 0" fill="none" stroke="#d0121b" stroke-width="5"/>
  </svg>
</section>

<section class="services">
  <h2 class="section-title" style="top:44px">OUR SERVICES</h2>
  <div class="service" style="left:99px">
    <div class="thumb" role="img" aria-label="Group of students with laptops outdoors" style="background:linear-gradient(135deg,#7e8f5a,#c9b59a)"></div>
    <h3>STUDENTS</h3>
    <p>Sed ut perspiciatis unde omnis iste natus error sit voluptatem accusantium doloremque laudantium, totam rem aperiam, eaque ipsa quae ab</p>
  </div>
  <div class="service" style="left:445px">
    <div class="thumb" role="img" aria-label="Student with backpack and books in a park" style="background:linear-gradient(135deg,#5f8e2e,#b8d37a)"></div>
    <h3>SCHOOLS</h3>
    <p>Sed ut perspiciatis unde omnis iste natus error sit voluptatem accusantium doloremque laudantium, totam rem aperiam, eaque ipsa quae ab</p>
  </div>
  <div class="service" style="left:791px">
    <div class="thumb" role="img" aria-label="Advisor speaking to students in a lecture hall" style="background:linear-gradient(135deg,#b89a6e,#4a4d57)"></div>
    <h3>ADVISORS</h3>
    <p>Sed ut perspiciatis unde omnis iste natus error sit voluptatem accusantium doloremque laudantium, totam rem aperiam, eaque ipsa quae ab</p>
  </div>
</section>

<section class="how">
  <h2 class="section-title" style="top:70px">HOW IT WORKS</h2>
  <div class="step" style="left:87px">
    <svg width="160" height="160" role="img" aria-label="Illustration of a student at a laptop"><rect x="33" y="33" width="94" height="94" transform="rotate(45 80 80)" fill="#f6c433"/></svg>
    <h3>College Admissions</h3>
    <p>Neque porro quisquam est, qui dolorem ipsum quia dolor sit amet, consectetur, adipisci velit, sed quia non</p>
    <span class="more">READ MORE</span>
  </div>
  <div class="step" style="left:354px">
    <svg width="160" height="160" role="img" aria-label="Illustration of an online video lesson"><rect x="33" y="33" width="94" height="94" transform="rotate(45 80 80)" fill="#5fd0c4"/></svg>
    <h3>Member Resources</h3>
    <p>Neque porro quisquam est, qui dolorem ipsum quia dolor sit amet, consectetur, adipisci velit, sed quia non</p>
    <span class="more">READ MORE</span>
  </div>
  <div class="step" style="left:619px">
    <svg width="160" height="160" role="img" aria-label="Illustration of an advisor presenting to a group"><rect x="33" y="33" width="94" height="94" transform="rotate(45 80 80)" fill="#f0657a"/></svg>
    <h3>College advisors</h3>
    <p>Neque porro quisquam est, qui dolorem ipsum quia dolor sit amet, consectetur, adipisci velit, sed quia non</p>
    <span class="more">READ MORE</span>
  </div>
  <div class="step" style="left:878px">
    <svg width="160" height="160" role="img" aria-label="Illustration of a stack of books"><rect x="33" y="33" width="94" height="94" transform="rotate(45 80 80)" fill="#f6c433"/></svg>
    <h3>Learn</h3>
    <p>Neque porro quisquam est, qui dolorem ipsum quia dolor sit amet, consectetur, adipisci velit, sed quia non</p>
    <span class="more">READ MORE</span>
  </div>
</section>

<section class="testimonial">
  <div class="avatar" role="img" aria-label="Portrait of the reviewer"></div>
  <p class="quote">“ Sed ut perspiciatis unde omnis iste natus error sit voluptatem accusantium doloremque laudantium, totam rem aperiam, eaque ipsa quae ab illo inventore veritatis et quasi architecto beatae vitae dicta sunt explicabo. Nemo enim ipsam voluptatem quia voluptas sit aspernatur aut odit aut fugit, sed quia consequuntur</p>
  <p class="quote-name">Mira Castell, The Bright Lantern</p>
  <div class="dots"><span></span><span></span><span></span></div>
  <div class="quote-mark">”</div>
</section>

<section class="news">
  <h2 class="section-title" style="top:64px">LATEST NEWS</h2>
  <article class="card" style="left:119px">
    <div class="thumb" role="img" aria-label="Student in a red jacket working on a laptop outdoors" style="background:linear-gradient(135deg,#8fa866,#c8453f 55%,#d9d3c4)"></div>
    <h3>Here's a sneak peek at what we're working on....!</h3>
    <div class="meta"><svg width="11" height="11"><rect x=".5" y="1.5" width="10" height="9" fill="none" stroke="#555"/><rect x=".5" y="1.5" width="10" height="3" fill="#555"/></svg>September 29, 2016 by Dana Whitfield</div>
    <p>The Bright Lantern is a new web site designed to provide a meeting place for college and university admissions officers and non-traditional applicants like homeschoolers, unschoolers, students who attend</p>
  </article>
  <article class="card" style="left:623px">
    <div class="thumb" role="img" aria-label="Student sitting on grass with a laptop and backpack" style="background:linear-gradient(180deg,#a9c07c,#5c8a35)"></div>
    <h3>Here's a sneak peek at what we're working on....!</h3>
    <div class="meta"><svg width="11" height="11"><rect x=".5" y="1.5" width="10" height="9" fill="none" stroke="#555"/><rect x=".5" y="1.5" width="10" height="3" fill="#555"/></svg>September 29, 2016 by Dana Whitfield</div>
    <p>The Bright Lantern is a new web site designed to provide a meeting place for college and university admissions officers and non-traditional applicants like homeschoolers, unschoolers, students who attend</p>
  </article>
</section>

<footer class="site-footer">
  <div class="f-col" style="left:99px">
    <h4>QUICK LINKS</h4>
    <ul class="f-links">
      <li>›&nbsp; Home</li><li>›&nbsp; Students</li><li>›&nbsp; Schools</li><li>›&nbsp; Advisors</li><li>›&nbsp; Member Resources</li><li>›&nbsp; News</li><li>›&nbsp; Contact Us</li>
    </ul>
  </div>
  <div class="f-col" style="left:306px">
    <h4>CONTACT INFO</h4>
    <div class="f-contact">
      <div><svg width="10" height="14" viewBox="0 0 10 14"><path d="M5 0a5 5 0 0 1 5 5c0 3.5-5 9-5 9S0 8.5 0 5a5 5 0 0 1 5-5z" fill="#fff"/><circle cx="5" cy="5" r="2" fill="#0f2b52"/></svg><span>The Bright Lantern 12 Harbor Lane<br>04410 Easton Vale</span></div>
      <div><svg width="13" height="13" viewBox="0 0 13 13"><path d="M2 0l3 3-1.5 2a8 8 0 0 0 4.5 4.5L10 8l3 3-2 2C5 13 0 8 0 2z" fill="#fff"/></svg><span>Phone : (+111) 555-0142</span></div>
      <div><svg width="14" height="11" viewBox="0 0 14 11"><rect x=".7" y=".7" width="12.6" height="9.6" fill="none" stroke="#fff" stroke-width="1.4"/><path d="M1 1l6 5 6-5" fill="none" stroke="#fff" stroke-width="1.4"/></svg><span>Email: info@brightlanternhub.example</span></div>
    </div>
  </div>
  <div class="f-col f-news" style="left:627px">
    <h4>JOIN OUR NEWSLETTER</h4>
    <p>Excepteur sint occaecat cupidatat non proident, sunt in culpa qui</p>
    <div class="f-input">Enter Name</div>
    <span class="f-btn">SUBSCRIBE</span>
  </div>
  <div class="f-col" style="left:977px">
    <h4>SOCIAL MEDIA</h4>
    <ul class="f-links f-social">
      <li><i></i>Community</li><li><i></i>Updates</li><li><i></i>Network</li><li><i></i>Videos</li>
    </ul>
  </div>
  <div class="copyright">© 2017 The Bright Lantern. All Rights Reserved.</div>
</footer>

</body>
</html>
```